Indie author needs a minimalist book cover

I need a book cover for my latest book on personal finance and investing. The book is called, "The Quiet Margin: Lessons on Steady Wealth, Calm Careers, and a Full Table". This is volume one of a three part series on the FI/RE movement, which stands for 'Financial Independence/Retire Early'. This book is on the foundational principles of FI/RE and details the specific steps that these 'Quiet Margin' involved in this community have done to position themselves to retire from paid work and live the life of their dreams - many only in their 20's, 30's and early 40's.

Title: The Quiet Margin
Author: RK Brenner
Volume 1: Foundations
Book dimensions: 6"x9"

Book Blurb (for back cover):

Let's face it, no one wants to be different. But sometimes following the 'normal' crowd gets you no further than that crowd.

When it comes to money, the normal crowd is your typical consumer. Deep in debt, struggling to make ends meet, but still spending money on the newest 'thing' that just came out.

But there's another group that's been forming - right on the fringes of the personal finance world. I call them The Quiet Margin. This book is about these superheroes of personal finance.

In it, you will learn:
• Who The Quiet Margin are and what is this FI/RE Movement they are apart of
• What basic strategy they use to control their money
• How they became debt-free - and how you can join them
• How to use the Tidewell Lever to help you really move the needle towards financial independence
• How to diversify your income with a side-hustle and which one to choose
• The quiet margin savings plan that will allow you to reach financial independence in ten years or less

This first book in The Quiet Margin series is about building a solid foundation so you and your family can become Quiet Margin, reach financial freedom, retire early, and live a rich life.

Target Market(s)

Individuals looking to take control of their money, reach financial independence, and retire early.

Font styles to use
Sans Serif
Other font styles liked:
• Arvo

Colors

Designer to choose colors to be used in the design.

Requirements
Must have
• A minimalist design (see examples), the title of the book, my author name, and the volume number and name (see below).
• My vision for the cover is to have a way to represent an 'outlier' in a simple, minimalistic way. I'm not set on any specific design - I'm open to what the designers come up with; I don't want to hold back anyone's creativity.
• Title: The Quiet Margin
• Author: RK Brenner
• Volume 1: Foundations
• Book Blurb (for back cover):
• Let's face it, no one wants to be different. But sometimes following the 'normal' crowd gets you no further than that crowd.
• When it comes to money, the normal crowd is your typical consumer. Deep in debt, struggling to make ends meet, but still spending money on the newest 'thing' that just came out.
• But there's another group that's been forming - right on the fringes of the personal finance world. I call them The Quiet Margin. This book is about these superheroes of personal finance.
• In it, you will learn:
• • Who The Quiet Margin are and what is this FI/RE Movement they are apart of
• • What basic strategy they use to control their money
• • How they became debt-free - and how you can join them
• • How to use the Tidewell Lever to help you really move the needle towards financial independence
• • How to diversify your income with a side-hustle and which one to choose
• • The quiet margin savings plan that will allow you to reach financial independence in ten years or less
• This first book in The Quiet Margin series is about building a solid foundation so you and your family can become Quiet Margin, reach financial freedom, retire early, and live a rich life.
Nice to have
• The subtitle - but only if it's not too crowded. Like I said before, I'm more interested in maintaining a minimalist aesthetic.
• The subtitle is: "Lessons on Steady Wealth, Calm Careers, And A Full Table"
Should not have
• Too many colors or objects on the cover.

```html
<!DOCTYPE html>
<html lang="en">
<head>
<meta charset="utf-8">
<title>The Quiet Margin — Volume 1: Foundations</title>
<link href="https://fonts.googleapis.com/css2?family=Carlito:wght@400;700&family=Cardo:wght@400&display=swap" rel="stylesheet">
<style>
  :root {
    --paper: #f1f0ed;
    --paper-shade: #e6e4df;
    --ink: #111111;
    --ink-soft: #5a5858;
    --title-ink: #3b3636;
    --rule: #6a6a6a;
    --ivory: #ece6d8;
    --ivory-deep: #d9cfbb;
    --gold: #d6a92e;
    --gold-deep: #9c6f12;
    --velvet: #8e1d1d;
  }
  * { margin: 0; padding: 0; box-sizing: border-box; }
  html, body { width: 1200px; height: 881px; overflow: hidden; }
  body { background: var(--paper); }
  .cover-spread {
    position: relative;
    width: 1200px;
    height: 881px;
    background: radial-gradient(ellipse at 50% 50%, var(--paper) 60%, var(--paper-shade) 100%);
    font-family: "Carlito", "Calibri", sans-serif;
    color: var(--ink);
  }

  /* Back cover */
  .back-cover {
    position: absolute;
    left: 47px;
    top: 72px;
    width: 511px;
    font-size: 16.5px;
    line-height: 20px;
  }
  .blurb {
    text-align: justify;
    text-align-last: center;
    margin-bottom: 19px;
  }
  .learn-list {
    font-weight: 700;
    text-align: center;
    list-style: none;
    margin-bottom: 39px;
  }

  /* Front cover */
  .front-cover {
    position: absolute;
    left: 660px;
    top: 0;
    width: 485px;
    height: 881px;
    text-align: center;
  }
  .volume-label {
    position: absolute;
    top: 35px;
    left: 0;
    width: 485px;
    font-size: 17px;
    letter-spacing: 0.62em;
    color: var(--ink-soft);
    padding-left: 0.62em;
  }
  .volume-rule {
    position: absolute;
    top: 76px;
    left: 30px;
    width: 425px;
    height: 1px;
    background: var(--rule);
  }
  .subtitle {
    position: absolute;
    top: 91px;
    left: 0;
    width: 485px;
    font-size: 21px;
    line-height: 32px;
    text-transform: uppercase;
    color: var(--ink-soft);
  }
  .title {
    position: absolute;
    top: 186px;
    left: -20px;
    width: 525px;
    font-family: "Cardo", Georgia, serif;
    font-weight: 400;
    font-size: 94px;
    line-height: 95px;
    color: var(--title-ink);
  }
  .author {
    position: absolute;
    top: 783px;
    left: 0;
    width: 485px;
    font-size: 36px;
    color: var(--ink);
  }

  .crown {
    position: absolute;
    border-radius: 30% 30% 14% 14%;
  }
  .crown--faint {
    background: linear-gradient(180deg, var(--ivory) 0%, var(--ivory-deep) 100%);
    opacity: 0.55;
  }
  .crown--pale {
    background: linear-gradient(180deg, var(--ivory) 0%, var(--ivory-deep) 100%);
    opacity: 0.9;
  }
  .crown--gold {
    background: radial-gradient(ellipse at 50% 35%, var(--velvet) 0%, var(--velvet) 28%, var(--gold) 48%, var(--gold-deep) 100%);
    border-radius: 40% 40% 18% 18%;
  }
</style>
</head>
<body>
<main class="cover-spread">

  <section class="back-cover">
    <p class="blurb">Let's face it, no one wants to be different. But sometimes following the 'normal' crowd gets you no further than that crowd.</p>
    <p class="blurb">When it comes to money, the normal crowd is your typical consumer. Deep in debt, struggling to make ends meet, but still spending money on the newest 'thing' that just came out.</p>
    <p class="blurb">But there's another group that's been forming- right on the fringes of the personal finance world. I call them the Quiet Margin. This book is about these superheroes of personal finance.</p>
    <ul class="learn-list">
      <li>In it, you will learn:</li>
      <li>• Who the quiet margin are and what is this<br>FI/RE Movement they are apart of</li>
      <li>• What basic strategy they use to control their money</li>
      <li>• How they became debt-free - and how you can join them</li>
      <li>• How to use the Tidewell Lever to help you really<br>move the needle towards financial independence</li>
      <li>• How to diversify your income with a side-hustle and<br>which one to choose</li>
      <li>• The quiet margin savings plan that will allow you to reach<br>financial independence in ten years or less</li>
    </ul>
    <p class="blurb">This first book in The Quiet Margin series is about building a solid foundation so you and your family can become quiet margin, reach financial freedom, retire early, and live a rich life.</p>
  </section>

  <section class="front-cover">
    <p class="volume-label">VOLUME 1: FOUNDATIONS</p>
    <div class="volume-rule"></div>
    <p class="subtitle">Lessons on Steady Wealth,<br>Calm Careers, and a Full Table</p>
    <h1 class="title">The Quiet<br>Margin</h1>

    <div class="crown crown--faint" style="left:113px;top:415px;width:62px;height:40px;" role="img" aria-label="Small faded ivory crown"></div>
    <div class="crown crown--faint" style="left:203px;top:415px;width:64px;height:40px;" role="img" aria-label="Small faded ivory crown"></div>
    <div class="crown crown--faint" style="left:287px;top:415px;width:63px;height:40px;" role="img" aria-label="Small faded ivory crown"></div>
    <div class="crown crown--pale" style="left:28px;top:460px;width:110px;height:70px;" role="img" aria-label="Ivory crown"></div>
    <div class="crown crown--pale" style="left:188px;top:460px;width:110px;height:70px;" role="img" aria-label="Ivory crown"></div>
    <div class="crown crown--pale" style="left:330px;top:460px;width:112px;height:70px;" role="img" aria-label="Ivory crown"></div>
    <div class="crown crown--gold" style="left:110px;top:535px;width:265px;height:200px;" role="img" aria-label="Large jewelled gold crown with red velvet, standing apart from the ivory crowns"></div>

    <p class="author">RK Brenner</p>
  </section>

</main>
</body>
</html>
```